Advertising flyer for proofreading business.

Hello everyone,

I need an advertising flyer for a new proofreading company in Australia.

I would like your design in be in two sizes:
- A4 (to be posted on noticeboards),
- A6 (to be printed in larger quantity to give away)
(please see the size specification file attached).

The text file is attached (Ad Text) and it contains lots of information. Please feel free to include your choice of text from the text file, but please include Poster title, and highlight 'ESL' and students discounts.

I understand that it is impossible to include the same amount of information on A6 and A4, so please feel free to chose what fits on each of them, but please keep the design similar.

I have attached our company logo, but feel free to adjust it to the poster design (feel free to change the color as well). The original logo file contains circle around it, please feel free to remove it and include only the typeset as it can be seen here: http://www.lexmarka.com.au/.

Flyers will be printed, so please see the specification file for details.

I will do my best to respond to feedback as soon as possible.

I appreciate your participation, time and help,
Best wishes,
Bartosz

Target Market(s)

Students, authors

Industry/Entity Type

Business

Colors

Designer to choose colors to be used in the design.

Requirements
Must have
• It would be good if poster is easy to spot on busy noticeboards and attract attention.
• Please keep the poster in the positive/optimistic mood, and so that it focuses on students, maybe photos of graduates(?).
• Poster title,
• Please include the list of proof-read documents as they are described in the attached text file (Ad Text).
• Please highlight students discounts and ESL.
Nice to have
• I would like to leave the creative freedom to all designers so at this point I have not adjusted the Look and Feel sliders. Please feel free to offer your own take on this.
• It would be nice if most of the text could be fit to the poster.

```html
<!DOCTYPE html>
<html lang="en">
<head>
<meta charset="utf-8">
<title>Lexmarka – Professional Proofreading Services</title>
<link rel="stylesheet" href="https://fonts.googleapis.com/css2?family=Montserrat:wght@400;500;600;700;800&family=Nunito+Sans:wght@400;600;700&display=swap">
<style>
  :root {
    --green: #3fae91;
    --green-dark: #2f9479;
    --ink: #1f1d1e;
    --footer: #262223;
    --band: #e4e4e4;
    --paper: #ffffff;
    --backdrop: #ececec;
    --photo-a: #5a5a5a;
    --photo-b: #141414;
  }
  * { box-sizing: border-box; margin: 0; padding: 0; }
  html, body { width: 1200px; height: 1000px; overflow: hidden; }
  body {
    background: var(--backdrop);
    font-family: "Nunito Sans", Arial, sans-serif;
    color: var(--ink);
    position: relative;
  }
  .flyer {
    position: absolute;
    left: 260px; top: 19px;
    width: 680px; height: 962px;
    background: var(--paper);
    overflow: hidden;
    box-shadow: 0 2px 10px rgba(0,0,0,.15);
  }
  .hero-photo {
    position: absolute; left: 0; top: 152px;
    width: 680px; height: 215px;
    background: radial-gradient(ellipse at 45% 35%, var(--photo-a), var(--photo-b) 80%);
    clip-path: polygon(0 0, 100% 0, 100% 165px, 50% 100%, 0 165px);
  }
  .masthead {
    position: absolute; left: 0; top: 0;
    width: 680px; height: 199px;
    background: var(--green);
    clip-path: polygon(0 0, 100% 0, 100% 152px, 50% 100%, 0 152px);
  }
  .brand {
    position: absolute; top: 62px; left: 0; width: 100%;
    display: flex; justify-content: center; align-items: center; gap: 12px;
    font-family: "Montserrat", sans-serif;
    font-weight: 400; font-size: 58px; line-height: 70px; color: #fff;
  }
  .brand-dot { width: 18px; height: 18px; border-radius: 50%; background: #fff; }
  .title {
    position: absolute; top: 244px; left: 0; width: 100%;
    text-align: center;
    font-family: "Montserrat", sans-serif; font-weight: 800;
    font-size: 30px; line-height: 36px; color: #fff; letter-spacing: .5px;
  }
  .intro {
    position: absolute; top: 380px; left: 50px; width: 580px;
    text-align: center;
    font-family: "Montserrat", sans-serif; font-weight: 600;
    font-size: 11.5px; line-height: 14px;
  }
  .intro p { margin-bottom: 13px; }
  .accent { color: var(--green); }
  .doc-types {
    position: absolute; top: 482px; left: 0; width: 100%; height: 120px;
    background: var(--band);
    border-top: 2px solid var(--green);
    border-bottom: 2px solid var(--green);
    padding: 3px 60px 0 67px;
  }
  .section-heading {
    font-family: "Montserrat", sans-serif; font-weight: 600;
    color: var(--green); font-size: 19px; line-height: 24px; letter-spacing: .3px;
  }
  .doc-types .section-heading { text-align: center; }
  .doc-list {
    list-style: none;
    display: grid; grid-template-columns: 288px 262px;
    column-gap: 4px; row-gap: 6px; margin-top: 4px;
    font-size: 11.5px; line-height: 14px;
  }
  .doc-list li, .price-list li { display: flex; gap: 4px; }
  .doc-list li.centered { grid-column: 1 / 3; justify-content: center; }
  .tick { flex: none; width: 12px; height: 12px; margin-top: 1px; }
  .price-guide {
    position: absolute; top: 617px; left: 55px; width: 320px;
  }
  .price-guide .section-heading { margin-bottom: 2px; }
  .price-list { list-style: none; font-size: 11.5px; line-height: 16px; }
  .price-list li { margin-bottom: 16px; }
  .testimonial {
    position: absolute; left: 415px; top: 638px;
    width: 234px; height: 189px;
    background: var(--green); border-radius: 14px;
    padding: 12px 12px 0 26px; color: #fff;
  }
  .quote-mark {
    position: absolute; left: 12px; top: -4px;
    font-family: Georgia, serif; font-size: 90px; line-height: 1;
    color: var(--green-dark);
  }
  .testimonial blockquote {
    position: relative;
    font-family: "Montserrat", sans-serif; font-size: 12.5px; line-height: 17px;
  }
  .testimonial cite {
    display: block; margin-top: 10px;
    font-style: normal; font-size: 9.5px; line-height: 11px; opacity: .85;
  }
  .contact-bar {
    position: absolute; left: 0; top: 879px; width: 100%; height: 83px;
    background: var(--footer); border-top: 4px solid var(--green);
    text-align: center; color: #fff;
    font-family: "Montserrat", sans-serif;
  }
  .contact-lead { font-size: 13px; margin-top: 10px; color: #ddd; }
  .contact-lead strong { color: #fff; font-weight: 600; }
  .contact-lines {
    display: flex; justify-content: center; align-items: center; gap: 10px;
    font-size: 20px; font-weight: 500; margin-top: 6px;
  }
  .phone-icon { width: 16px; height: 16px; }
</style>
</head>
<body>
<article class="flyer">
  <div class="hero-photo" role="img" aria-label="Dark monochrome photo of graduates raising their hands in celebration"></div>
  <header class="masthead"></header>
  <div class="brand"><span class="brand-dot"></span>Lexmarka</div>
  <h1 class="title">PROFESSIONAL&nbsp; PROOFREADING<br>SERVICES</h1>

  <section class="intro">
    <p>Help with English as a second language <span class="accent">(ESL - native English speaker with English Honours degree</span> will correct all English language errors, spelling and grammar mistakes.</p>
    <p>Includes referencing and editing for style, coherence and clarity</p>
    <p>Fast, negotiable time-frames.</p>
  </section>

  <section class="doc-types">
    <h2 class="section-heading">TYPES OF PROOF-READ DOCUMENTS:</h2>
    <ul class="doc-list">
      <li><svg class="tick" viewBox="0 0 12 12"><path d="M1 6.5l3 3 7-8" fill="none" stroke="#3fae91" stroke-width="2"/></svg>essays / assignments / theses / resumes</li>
      <li><svg class="tick" viewBox="0 0 12 12"><path d="M1 6.5l3 3 7-8" fill="none" stroke="#3fae91" stroke-width="2"/></svg>advertising copy / brochures / catalogues / media releases</li>
      <li><svg class="tick" viewBox="0 0 12 12"><path d="M1 6.5l3 3 7-8" fill="none" stroke="#3fae91" stroke-width="2"/></svg>business correspondence / training manuals / newsletters</li>
      <li><svg class="tick" viewBox="0 0 12 12"><path d="M1 6.5l3 3 7-8" fill="none" stroke="#3fae91" stroke-width="2"/></svg>websites / presentations / speeches</li>
      <li class="centered"><svg class="tick" viewBox="0 0 12 12"><path d="M1 6.5l3 3 7-8" fill="none" stroke="#3fae91" stroke-width="2"/></svg>novels / short stories</li>
    </ul>
  </section>

  <section class="price-guide">
    <h2 class="section-heading">PRICE GUIDE:</h2>
    <ul class="price-list">
      <li><svg class="tick" viewBox="0 0 12 12"><path d="M1 6.5l3 3 7-8" fill="none" stroke="#3fae91" stroke-width="2"/></svg><span>Prices starting at <span class="accent">$20 per page.</span> Additional charges may apply for longer and/or more complex documents (e.g. documents requiring specialist help with English as a second language).</span></li>
      <li><svg class="tick" viewBox="0 0 12 12"><path d="M1 6.5l3 3 7-8" fill="none" stroke="#3fae91" stroke-width="2"/></svg><span>Discounts for not-for-profit organisations and students. <span class="accent">Special student discount rate: $25 per hour - roughly 1000 words (4 pages) of well-written text.</span></span></li>
      <li><svg class="tick" viewBox="0 0 12 12"><path d="M1 6.5l3 3 7-8" fill="none" stroke="#3fae91" stroke-width="2"/></svg><span>Package deals on documents <span class="accent">over 50,000 words.</span></span></li>
      <li><svg class="tick" viewBox="0 0 12 12"><path d="M1 6.5l3 3 7-8" fill="none" stroke="#3fae91" stroke-width="2"/></svg><span class="accent">Fast turnaround times (same day service can be provided by special arrangement).</span></li>
    </ul>
  </section>

  <aside class="testimonial">
    <span class="quote-mark">&ldquo;</span>
    <blockquote>Hannah understood our requirements quickly and has been fantastic at delivering quality work, on time and within agreed budget. It's a pleasure to work with her.&rdquo;</blockquote>
    <cite>Clara Dunn<br>Operations Manager<br>Orbis Training AU</cite>
  </aside>

  <footer class="contact-bar">
    <p class="contact-lead">Contact Us For An <strong>Obligation-Free Quote:</strong></p>
    <p class="contact-lines">
      <svg class="phone-icon" viewBox="0 0 16 16"><circle cx="8" cy="8" r="7" fill="none" stroke="#3fae91" stroke-width="1.5"/><path d="M5.5 4.5l1.3-.3.8 1.8-.9.7a5 5 0 0 0 2.4 2.4l.7-.9 1.8.8-.3 1.3c-3.2.2-6-2.6-5.8-5.8z" fill="#3fae91"/></svg>
      <span>0400 218 366</span><span>|</span><span>proofing@lexmarka.com.au</span>
    </p>
  </footer>
</article>
</body>
</html>
```